BUsiness Card

We need a unique business card design for a new aesthetic practice, Meadowlark Skin & Vitality, P.A. The reverse of the card should be an appointment card.

```html
<!DOCTYPE html>
<html lang="en">
<head>
<meta charset="utf-8">
<title>Meadowlark Skin & Vitality – Business & Appointment Card</title>
<link href="https://fonts.googleapis.com/css2?family=Crimson+Text:wght@400;600;700&family=Lato:wght@700&display=swap" rel="stylesheet">
<style>
  :root {
    --stage: #2b2b2d;
    --navy: #0e4a6a;
    --navy-deep: #0b3f5c;
    --teal: #5cc3bd;
    --white: #ffffff;
    --paper: #fdfdfd;
    --serif: "Crimson Text", Georgia, serif;
    --sans: "Lato", Arial, sans-serif;
  }
  * { box-sizing: border-box; margin: 0; padding: 0; }
  html, body { width: 1200px; height: 900px; overflow: hidden; }
  body { background: var(--stage); font-family: var(--serif); position: relative; }

  .card {
    position: absolute;
    left: 260px;
    width: 680px;
    height: 388px;
    overflow: hidden;
    box-shadow: 0 10px 28px rgba(0,0,0,.45);
  }

  /* ---------- appointment side ---------- */
  .card--appointment { top: 40px; background: var(--navy); color: var(--white); }
  .appointment__halo {
    position: absolute; right: 70px; top: 70px;
    width: 210px; height: 210px; border-radius: 50%;
    background: rgba(255,255,255,.07);
  }
  .label {
    display: inline-block;
    background: var(--white); color: var(--navy);
    font-weight: 700; letter-spacing: .5px;
    text-transform: uppercase; line-height: 1;
  }
  .appointment__title { position: absolute; left: 210px; top: 40px; font-size: 19px; padding: 5px 10px; }
  .field { position: absolute; font-size: 17px; white-space: nowrap; }
  .field .dots { letter-spacing: 3px; }
  .field--date { left: 50px; top: 118px; }
  .field--time { left: 360px; top: 118px; }
  .check { position: absolute; display: flex; align-items: center; gap: 5px; font-size: 17px; }
  .box { width: 24px; height: 20px; border: 2px solid var(--white); border-radius: 3px; }
  .ampm { top: 80px; }
  .days { top: 190px; }
  .appointment__policy-title { position: absolute; left: 230px; top: 258px; font-size: 16px; padding: 4px 9px; }
  .appointment__policy {
    position: absolute; left: 90px; right: 90px; top: 292px;
    text-align: center; font-size: 16px; line-height: 1.3;
  }

  /* ---------- contact side ---------- */
  .card--contact { top: 472px; background: var(--paper); }
  .contact__waves { position: absolute; inset: 0; }
  .brand { position: absolute; right: 40px; top: 38px; display: flex; align-items: center; gap: 14px; }
  .brand__dot { width: 46px; height: 46px; border-radius: 50%; background: var(--navy); }
  .brand__name { font-size: 27px; font-weight: 600; color: var(--navy); line-height: 1.05; }
  .person { position: absolute; left: 60px; top: 250px; color: var(--white); }
  .person__name { font-size: 27px; font-weight: 700; line-height: 1; }
  .person__role { font-size: 17px; margin-top: 3px; }
  .contact-list { list-style: none; margin-top: 12px; font-size: 15px; }
  .contact-list li { display: flex; align-items: center; gap: 9px; line-height: 1.45; }
  .contact-list svg { width: 14px; height: 14px; fill: var(--white); }
  .address {
    position: absolute; right: 40px; top: 270px;
    font-family: var(--sans); font-weight: 700; font-size: 15px;
    color: var(--white); text-align: right; line-height: 1.35;
  }
</style>
</head>
<body>

<section class="card card--appointment" aria-label="Appointment card">
  <div class="appointment__halo" aria-hidden="true"></div>
  <h2 class="label appointment__title">Next Appointment</h2>

  <div class="check ampm" style="left:500px">AM <span class="box"></span></div>
  <div class="check ampm" style="left:580px">PM <span class="box"></span></div>

  <div class="field field--date">Date: <span class="dots">.........................</span></div>
  <div class="field field--time">Time: <span class="dots">....................</span></div>

  <div class="check days" style="left:50px">Mon <span class="box"></span></div>
  <div class="check days" style="left:138px">Tue <span class="box"></span></div>
  <div class="check days" style="left:222px">Wed <span class="box"></span></div>
  <div class="check days" style="left:310px">Thu <span class="box"></span></div>
  <div class="check days" style="left:392px">Fri <span class="box"></span></div>
  <div class="check days" style="left:468px">Sat <span class="box"></span></div>
  <div class="check days" style="left:550px">Sun <span class="box"></span></div>

  <h3 class="label appointment__policy-title">Cancellation Policy</h3>
  <p class="appointment__policy">If you are unable to keep your appointment, please provide at least 2 business days notice or a full visit fee will apply.</p>
</section>

<section class="card card--contact" aria-label="Business card">
  <svg class="contact__waves" viewBox="0 0 680 388" preserveAspectRatio="none" aria-hidden="true">
    <path d="M0,250 C160,175 330,150 520,150 C600,150 650,120 680,95 L680,110 C640,140 600,162 520,164 C340,168 170,200 0,275 Z" fill="var(--teal)"/>
    <path d="M0,282 C170,205 340,178 520,172 C600,170 650,140 680,112 L680,388 L0,388 Z" fill="var(--navy)"/>
    <path d="M260,200 C400,176 520,178 640,120" fill="none" stroke="var(--white)" stroke-width="2" opacity=".9"/>
    <path d="M350,190 C470,178 560,176 660,135" fill="none" stroke="var(--white)" stroke-width="1.2" opacity=".7"/>
  </svg>

  <div class="brand">
    <span class="brand__dot" aria-hidden="true"></span>
    <span class="brand__name">Meadowlark Skin<br>&amp; Vitality, P.A.</span>
  </div>

  <div class="person">
    <p class="person__name">Lena Halvorsen</p>
    <p class="person__role">Owner / Founder</p>
    <ul class="contact-list">
      <li><svg viewBox="0 0 24 24"><path d="M6.6 10.8a15.1 15.1 0 0 0 6.6 6.6l2.2-2.2a1 1 0 0 1 1-.25 11.4 11.4 0 0 0 3.6.57 1 1 0 0 1 1 1V20a1 1 0 0 1-1 1A17 17 0 0 1 3 4a1 1 0 0 1 1-1h3.5a1 1 0 0 1 1 1c0 1.25.2 2.45.57 3.57a1 1 0 0 1-.25 1z"/></svg>555.204.3180</li>
      <li><svg viewBox="0 0 24 24"><path d="M2 5h20v14H2zM3.5 6.5 12 13l8.5-6.5v-.1h-17z"/></svg>hello@meadowlark-skin.com</li>
      <li><svg viewBox="0 0 24 24"><circle cx="12" cy="12" r="10"/></svg>www.meadowlark-skin.com</li>
    </ul>
  </div>

  <p class="address">1180 Harbor View Blvd #310<br>Palm Isle, Florida 33400</p>
</section>

</body>
</html>
```